Anzeigengestaltung für Steuerberaterin
Zielgruppe
Ich bin Steuerberaterin und Zertizierter Testamentsvollstrecker (BKW) in Gerlingen.
Wir sind keine kleine, innovative Steuerkanzlei und möchten vor allem Mandanten ansprechen, den eine digitale Zusammenarbeit wichtig ist.
Zielgruppe: Startups, kleine Unternehmen oder Freiberufler, Gemeinnützige Organisationen
Software: Datev, Buchhaltungsbutler, sevDesk
Aufgabenstellung
Nach meinem Umzug in größere Büroräume benötige ich eine Anzeige im Format 90 x 80 mm für eine Zeitung.
Auf der Anzeige sollte ein Umzugshinweis enthalten sein. Die Anzeige würde ich gerne wieder verwenden. (eine version ohne Umzugshinweis)
Slogan: Gemeinsam Steuern Gestalten

```html
<!DOCTYPE html>
<html lang="de">
<head>
<meta charset="utf-8">
<title>Anzeige Steuerkanzlei – Varianten</title>
<link rel="stylesheet" href="https://fonts.googleapis.com/css2?family=Roboto:wght@300;400;500;700;900&display=swap">
<style>
  :root {
    --brand-blue: #1a4f9f;
    --text-grey: #666666;
    --ink: #111111;
    --panel-grey: #eeeeee;
    --paper: #ffffff;
    --ribbon-green: #4aa832;
    --ribbon-maroon: #6b0f08;
  }
  * { box-sizing: border-box; margin: 0; padding: 0; }
  html, body { width: 849px; height: 1200px; overflow: hidden; }
  body {
    position: relative;
    font-family: "Roboto", Arial, sans-serif;
    background: var(--paper);
    color: var(--ink);
  }
  .column { position: absolute; top: 0; height: 1200px; }
  .column--umzug { left: 0; width: 424px; background: var(--paper); }
  .column--normal { left: 424px; width: 425px; background: var(--panel-grey); }
  .column-title {
    position: absolute; top: 12px;
    font-size: 25px; font-weight: 400; letter-spacing: 0.5px;
  }
  .column--umzug .column-title { left: 50px; }
  .column--normal .column-title { left: 60px; }
  .version-label { position: absolute; font-size: 24px; font-weight: 400; }
  .column--umzug .version-label { left: 44px; }
  .column--normal .version-label { left: 65px; }

  .ad {
    position: absolute; width: 313px; height: 278px;
    background: var(--paper);
    box-shadow: 0 2px 6px rgba(0,0,0,0.35);
    overflow: hidden;
  }
  .column--umzug .ad { left: 44px; }
  .column--normal .ad { left: 65px; }
  .ad--v01::before {
    content: ""; position: absolute; left: 0; top: 0; bottom: 0; width: 8px;
    background: var(--brand-blue);
  }
  .ad--v02::after {
    content: ""; position: absolute; left: 0; right: 0; bottom: 0; height: 2px;
    background: var(--brand-blue);
  }
  .ad__inner { position: absolute; inset: 0; }
  .ad--v01 .ad__inner { left: 8px; }

  .slogan { position: absolute; left: 11px; top: 9px; line-height: 44px; font-size: 38px; font-weight: 500; letter-spacing: -0.2px; white-space: nowrap; }
  .ad--v02 .slogan, .ad--v03 .slogan { left: 13px; top: 9px; line-height: 46.5px; font-size: 40px; }
  .slogan__line { display: block; color: var(--text-grey); }
  .slogan__line--accent { color: var(--brand-blue); font-weight: 900; }

  .claim {
    position: absolute; left: 11px; top: 148px;
    font-size: 12.3px; font-weight: 300; line-height: 15px; color: var(--text-grey);
    white-space: nowrap;
  }
  .ad--v02 .claim, .ad--v03 .claim { left: 13px; top: 150px; }

  .firm-name {
    position: absolute; left: 10px; top: 214px; width: 110px;
    font-size: 11px; font-weight: 700; line-height: 14px; letter-spacing: 0.6px;
    color: var(--text-grey); text-align: center; text-transform: uppercase;
  }
  .firm-name::before {
    content: ""; display: block; width: 22px; height: 22px; margin: 0 auto 6px;
    background: var(--brand-blue);
  }
  .ad--v02 .firm-name, .ad--v03 .firm-name { left: 12px; }

  .contact {
    position: absolute; left: 137px; top: 206px;
    font-size: 8.6px; font-weight: 300; line-height: 13px; color: var(--text-grey);
    white-space: nowrap;
  }
  .ad--v01 .contact { left: 129px; }
  .contact__gap { display: block; height: 13px; }

  .ribbon { position: absolute; right: 0; top: 0; width: 104px; height: 104px; }
  .ribbon__text {
    font-family: "Roboto", Arial, sans-serif; font-size: 12px; font-weight: 700; fill: var(--paper);
  }
  .ribbon--green .ribbon__band { fill: var(--ribbon-green); }
  .ribbon--blue .ribbon__band { fill: var(--brand-blue); }
  .ribbon--maroon .ribbon__band { fill: var(--ribbon-maroon); }
</style>
</head>
<body>

<section class="column column--umzug">
  <h2 class="column-title">VARIANTE UMZUG</h2>

  <p class="version-label" style="top:64px">v01</p>
  <article class="ad ad--v01" style="top:102px">
    <div class="ad__inner">
      <h1 class="slogan"><span class="slogan__line">GEMEINSAM</span><span class="slogan__line slogan__line--accent">STEUERN</span><span class="slogan__line">GESTALTEN</span></h1>
      <p class="claim">Innovative, digitale Steuerberatung für Startups,<br>Unternehmen und gemeinnützige Organisationen.</p>
      <p class="firm-name">Steuerkanzlei<br>Lotte Krause</p>
      <p class="contact">Lindenhofer Str. 12/1 &nbsp;|&nbsp; 71234 Lindenau<br>T. 07123 / 98 21 400 &nbsp;|&nbsp; F. 07123 / 98 21 401<span class="contact__gap"></span>www.steuerkanzlei-krause.de<br>lotte.krause@steuerkanzlei-krause.de</p>
    </div>
    <svg class="ribbon ribbon--green" viewBox="0 0 104 104">
      <polygon class="ribbon__band" points="0,0 50,0 104,54 104,104"/>
      <g transform="translate(63,42) rotate(45)">
        <text class="ribbon__text" text-anchor="middle" y="-3">Wir sind</text>
        <text class="ribbon__text" text-anchor="middle" y="11">umgezogen!</text>
      </g>
    </svg>
  </article>

  <p class="version-label" style="top:459px">v02</p>
  <article class="ad ad--v02" style="top:495px">
    <div class="ad__inner">
      <h1 class="slogan"><span class="slogan__line">GEMEINSAM</span><span class="slogan__line slogan__line--accent">STEUERN</span><span class="slogan__line">GESTALTEN</span></h1>
      <p class="claim">Innovative, digitale Steuerberatung für Startups,<br>Unternehmen und gemeinnützige Organisationen.</p>
      <p class="firm-name">Steuerkanzlei<br>Lotte Krause</p>
      <p class="contact">Lindenhofer Str. 12/1 &nbsp;|&nbsp; 71234 Lindenau<br>T. 07123 / 98 21 400 &nbsp;|&nbsp; F. 07123 / 98 21 401<span class="contact__gap"></span>www.steuerkanzlei-krause.de<br>lotte.krause@steuerkanzlei-krause.de</p>
    </div>
    <svg class="ribbon ribbon--blue" viewBox="0 0 104 104">
      <polygon class="ribbon__band" points="0,0 50,0 104,54 104,104"/>
      <g transform="translate(63,42) rotate(45)">
        <text class="ribbon__text" text-anchor="middle" y="-3">Wir sind</text>
        <text class="ribbon__text" text-anchor="middle" y="11">umgezogen!</text>
      </g>
    </svg>
  </article>

  <p class="version-label" style="top:852px">v03</p>
  <article class="ad ad--v03" style="top:888px">
    <div class="ad__inner">
      <h1 class="slogan"><span class="slogan__line">GEMEINSAM</span><span class="slogan__line slogan__line--accent">STEUERN</span><span class="slogan__line">GESTALTEN</span></h1>
      <p class="claim">Innovative, digitale Steuerberatung für Startups,<br>Unternehmen und gemeinnützige Organisationen.</p>
      <p class="firm-name">Steuerkanzlei<br>Lotte Krause</p>
      <p class="contact">Lindenhofer Str. 12/1 &nbsp;|&nbsp; 71234 Lindenau<br>T. 07123 / 98 21 400 &nbsp;|&nbsp; F. 07123 / 98 21 401<span class="contact__gap"></span>www.steuerkanzlei-krause.de<br>lotte.krause@steuerkanzlei-krause.de</p>
    </div>
    <svg class="ribbon ribbon--maroon" viewBox="0 0 104 104">
      <polygon class="ribbon__band" points="0,0 50,0 104,54 104,104"/>
      <g transform="translate(63,42) rotate(45)">
        <text class="ribbon__text" text-anchor="middle" y="-3">Wir sind</text>
        <text class="ribbon__text" text-anchor="middle" y="11">umgezogen!</text>
      </g>
    </svg>
  </article>
</section>

<section class="column column--normal">
  <h2 class="column-title">VARIANTE NORMAL</h2>

  <p class="version-label" style="top:64px">v01</p>
  <article class="ad ad--v01" style="top:102px">
    <div class="ad__inner">
      <h1 class="slogan"><span class="slogan__line">GEMEINSAM</span><span class="slogan__line slogan__line--accent">STEUERN</span><span class="slogan__line">GESTALTEN</span></h1>
      <p class="claim">Innovative, digitale Steuerberatung für Startups,<br>Unternehmen und gemeinnützige Organisationen.</p>
      <p class="firm-name">Steuerkanzlei<br>Lotte Krause</p>
      <p class="contact">Lindenhofer Str. 12/1 &nbsp;|&nbsp; 71234 Lindenau<br>T. 07123 / 98 21 400 &nbsp;|&nbsp; F. 07123 / 98 21 401<span class="contact__gap"></span>www.steuerkanzlei-krause.de<br>lotte.krause@steuerkanzlei-krause.de</p>
    </div>
  </article>

  <p class="version-label" style="top:459px">v02</p>
  <article class="ad ad--v02" style="top:495px">
    <div class="ad__inner">
      <h1 class="slogan"><span class="slogan__line">GEMEINSAM</span><span class="slogan__line slogan__line--accent">STEUERN</span><span class="slogan__line">GESTALTEN</span></h1>
      <p class="claim">Innovative, digitale Steuerberatung für Startups,<br>Unternehmen und gemeinnützige Organisationen.</p>
      <p class="firm-name">Steuerkanzlei<br>Lotte Krause</p>
      <p class="contact">Lindenhofer Str. 12/1 &nbsp;|&nbsp; 71234 Lindenau<br>T. 07123 / 98 21 400 &nbsp;|&nbsp; F. 07123 / 98 21 401<span class="contact__gap"></span>www.steuerkanzlei-krause.de<br>lotte.krause@steuerkanzlei-krause.de</p>
    </div>
  </article>

  <p class="version-label" style="top:852px">v03</p>
  <article class="ad ad--v03" style="top:888px">
    <div class="ad__inner">
      <h1 class="slogan"><span class="slogan__line">GEMEINSAM</span><span class="slogan__line slogan__line--accent">STEUERN</span><span class="slogan__line">GESTALTEN</span></h1>
      <p class="claim">Innovative, digitale Steuerberatung für Startups,<br>Unternehmen und gemeinnützige Organisationen.</p>
      <p class="firm-name">Steuerkanzlei<br>Lotte Krause</p>
      <p class="contact">Lindenhofer Str. 12/1 &nbsp;|&nbsp; 71234 Lindenau<br>T. 07123 / 98 21 400 &nbsp;|&nbsp; F. 07123 / 98 21 401<span class="contact__gap"></span>www.steuerkanzlei-krause.de<br>lotte.krause@steuerkanzlei-krause.de</p>
    </div>
  </article>
</section>

</body>
</html>
```